Design Business Card with our Logo

We have changed our firm name from Halbrook, Tessing & Varn, PLLC to Halbrook, Tessing & Orlow, LLP and now need to re-design our business cards. I have attached an image of our old card so that you can see the style that we like -- clean, modern, colorful and professional. We were not thrilled with the fonts that we used on the old card, so feel free to use more modern fonts. I also attached a copy of the new logo shape, which is similar to the old one; and some other card ideas that we found in the gigmarto.com showcase that looked nice to us. Please feel free to try different colors as we are not tied down to orange or blue. Looking for fresh new ideas.

```html
<!DOCTYPE html>
<html lang="en">
<head>
<meta charset="utf-8">
<title>Halbrook, Tessing &amp; Orlow, LLP — Business Card</title>
<link rel="stylesheet" href="https://fonts.googleapis.com/css2?family=Cormorant+SC:wght@600&family=Lato:wght@400;700&display=swap">
<style>
  :root {
    --canvas: #e6e6e6;
    --ink: #141414;
    --card-dark: #111111;
    --paper: #ffffff;
    --accent: #f39a1e;
    --muted: #333333;
    --light: #ffffff;
  }
  * { box-sizing: border-box; margin: 0; padding: 0; }
  html, body { width: 1200px; height: 900px; overflow: hidden; }
  body {
    background: var(--canvas);
    font-family: "Lato", Arial, sans-serif;
    position: relative;
  }
  .card {
    position: absolute;
    width: 660px;
    height: 378px;
    left: 270px;
    border-radius: 4px;
    overflow: hidden;
    box-shadow: 0 10px 28px rgba(0,0,0,.18);
  }
  /* Front */
  .card-front { top: 52px; background: var(--card-dark); color: var(--light); }
  .front-brand {
    position: absolute; top: 92px; left: 0; right: 0;
    text-align: center;
    font-family: "Cormorant SC", Georgia, serif;
    font-weight: 600;
    font-size: 46px;
    line-height: 1;
    color: var(--accent);
  }
  .practice {
    position: absolute; left: 0; right: 0; bottom: 58px;
    text-align: center;
  }
  .practice-title {
    font-size: 16px; letter-spacing: .5px; text-transform: uppercase; margin-bottom: 8px;
  }
  .practice-list { font-size: 16px; color: var(--accent); }
  .practice-list .sep { color: var(--light); margin: 0 4px; }

  /* Back */
  .card-back { top: 470px; background: var(--paper); color: var(--ink); }
  .accent-strip {
    position: absolute; left: 0; right: 0; bottom: 0; height: 16px; background: var(--accent);
  }
  .firm {
    position: absolute; left: 42px; top: 138px;
    display: flex; align-items: center; gap: 18px;
  }
  .firm-mark { width: 26px; height: 26px; background: var(--accent); flex: none; }
  .firm-name {
    font-family: "Cormorant SC", Georgia, serif; font-weight: 600;
    font-size: 31px; line-height: .98; color: var(--ink);
  }
  .firm-tag { font-size: 15px; letter-spacing: .6px; text-transform: uppercase; margin-top: 4px; }

  .contact { position: absolute; left: 410px; top: 56px; width: 230px; }
  .block { position: relative; padding-left: 18px; }
  .block::before {
    content: ""; position: absolute; left: 0; top: 2px; bottom: 2px; width: 2px; background: var(--accent);
  }
  .person-name { font-size: 19px; font-weight: 700; text-transform: uppercase; color: var(--muted); }
  .person-name .first { color: var(--accent); }
  .person-role, .address { font-size: 14px; line-height: 1.3; color: var(--muted); }
  .address-block { margin-top: 18px; }
  .links { margin-top: 22px; }
  .links::before { background: var(--ink); }
  .links li {
    list-style: none; display: flex; align-items: center; gap: 7px;
    font-size: 14px; line-height: 1.35; color: var(--muted);
  }
  .links svg { width: 12px; height: 12px; fill: var(--accent); flex: none; }
</style>
</head>
<body>
  <section class="card card-front" aria-label="Card front">
    <p class="front-brand">Halbrook, Tessing<br>&amp; Orlow, LLP</p>
    <div class="practice">
      <p class="practice-title">Areas of Practice</p>
      <p class="practice-list">Real Estate and Construction<span class="sep">|</span>Business Disputes<span class="sep">|</span>Trial Litigation/Injury</p>
    </div>
  </section>

  <section class="card card-back" aria-label="Card back">
    <div class="firm">
      <span class="firm-mark" aria-hidden="true"></span>
      <div>
        <p class="firm-name">Halbrook<br>Tessing &amp;<br>Orlow, LLP</p>
        <p class="firm-tag">Attorneys at Law</p>
      </div>
    </div>

    <div class="contact">
      <div class="block">
        <p class="person-name"><span class="first">Daniel</span> Varga</p>
        <p class="person-role">Director</p>
      </div>
      <div class="block address-block">
        <p class="address">123 M Street Address<br>Suite-548 City, State 00000</p>
      </div>
      <ul class="block links">
        <li><svg viewBox="0 0 24 24" aria-hidden="true"><path d="M6.6 10.8a15 15 0 0 0 6.6 6.6l2.2-2.2c.3-.3.7-.4 1-.2 1.1.4 2.3.6 3.6.6.6 0 1 .4 1 1V20c0 .6-.4 1-1 1C10.6 21 3 13.4 3 4c0-.6.4-1 1-1h3.5c.6 0 1 .4 1 1 0 1.3.2 2.5.6 3.6.1.3 0 .7-.2 1z"/></svg>000-000-0000</li>
        <li><svg viewBox="0 0 24 24" aria-hidden="true"><path d="M7 2h10a2 2 0 0 1 2 2v16a2 2 0 0 1-2 2H7a2 2 0 0 1-2-2V4a2 2 0 0 1 2-2zm0 3v13h10V5zm5 14.2a1 1 0 1 0 0 2 1 1 0 0 0 0-2z"/></svg>000-000-0000</li>
        <li><svg viewBox="0 0 24 24" aria-hidden="true"><path d="M2 5h20v14H2zm2 2v.5l8 5 8-5V7zm0 2.8V17h16V9.8l-8 5z"/></svg>dan@vargamail.com</li>
        <li><svg viewBox="0 0 24 24" aria-hidden="true"><path d="M12 2a10 10 0 1 0 0 20 10 10 0 0 0 0-20zm6.9 9h-3a15 15 0 0 0-1.3-5.6A8 8 0 0 1 18.9 11zM12 4.1c.9 1.2 1.7 3.6 1.9 6.9h-3.8c.2-3.3 1-5.7 1.9-6.9zM9.4 5.4A15 15 0 0 0 8.1 11h-3a8 8 0 0 1 4.3-5.6zM5.1 13h3a15 15 0 0 0 1.3 5.6A8 8 0 0 1 5.1 13zm6.9 6.9c-.9-1.2-1.7-3.6-1.9-6.9h3.8c-.2 3.3-1 5.7-1.9 6.9zm2.6-1.3a15 15 0 0 0 1.3-5.6h3a8 8 0 0 1-4.3 5.6z"/></svg>www.danvarga.com</li>
      </ul>
    </div>
    <div class="accent-strip" aria-hidden="true"></div>
  </section>
</body>
</html>
```